Dune Air & Plus business card

I need an awesome, double-sided business card designed with our new logo. I would like the one side black with the colored logo, and the back side is all yours. I'd like to see horizontal and vertical layouts. Get creative! Thank you.

Target Market(s)

HVAC, Heating and Cooling in Phoenix, AZ

Industry/Entity Type

HVAC

Contact Information for Business Card

We need our new logo on the card. Tom Harker, (623) 555-0142, tom@trydunesair.com, www.trydunesair.com, ROC 514273

```html
<!DOCTYPE html>
<html lang="en">
<head>
<meta charset="utf-8">
<title>Dune Air &amp; Plus business card</title>
<link href="https://fonts.googleapis.com/css2?family=Poppins:wght@400;600;700&display=swap" rel="stylesheet">
<style>
  :root {
    --page: #e4e4e6;
    --card-black: #000000;
    --card-white: #ffffff;
    --brand-blue: #1a78d6;
    --text-light: #ffffff;
  }
  html, body {
    margin: 0;
    padding: 0;
    width: 1200px;
    height: 1200px;
    overflow: hidden;
    background: var(--page);
    font-family: "Poppins", sans-serif;
  }
  .canvas {
    position: relative;
    width: 1200px;
    height: 1200px;
  }
  .card {
    position: absolute;
    top: 468px;
    width: 486px;
    height: 277px;
    box-sizing: border-box;
  }
  .card--front {
    left: 82px;
    background: var(--card-black);
  }
  .card--back {
    left: 641px;
    background: var(--card-white);
  }
  .brand-name {
    position: absolute;
    left: 0;
    right: 0;
    display: flex;
    align-items: center;
    justify-content: center;
    gap: 10px;
    margin: 0;
    font-weight: 700;
    color: var(--brand-blue);
    white-space: nowrap;
  }
  .brand-name__dot {
    border-radius: 50%;
    background: var(--brand-blue);
    flex: none;
  }
  .card--front .brand-name {
    top: 118px;
    font-size: 34px;
    line-height: 40px;
  }
  .card--front .brand-name__dot { width: 26px; height: 26px; }
  .card--back .brand-name {
    top: 52px;
    font-size: 28px;
    line-height: 34px;
  }
  .card--back .brand-name__dot { width: 22px; height: 22px; }
  .contact-panel {
    position: absolute;
    left: 12px;
    top: 141px;
    width: 461px;
    height: 123px;
    border-radius: 13px;
    background: var(--card-black);
    color: var(--text-light);
  }
  .contact-panel__name {
    position: absolute;
    left: 41px;
    top: 45px;
    margin: 0;
    font-size: 25px;
    line-height: 32px;
    font-weight: 600;
  }
  .contact-list {
    position: absolute;
    left: 244px;
    top: 15px;
    margin: 0;
    padding: 0;
    list-style: none;
    font-size: 13.5px;
    font-weight: 400;
  }
  .contact-list__item {
    display: flex;
    align-items: center;
    height: 23.5px;
    white-space: nowrap;
  }
  .contact-list__icon {
    width: 11px;
    height: 11px;
    margin-right: 11px;
    fill: var(--text-light);
    flex: none;
  }
</style>
</head>
<body>
<main class="canvas">
  <section class="card card--front" aria-label="Card front">
    <p class="brand-name"><span class="brand-name__dot"></span>Dune Air &amp; Plus</p>
  </section>

  <section class="card card--back" aria-label="Card back">
    <p class="brand-name"><span class="brand-name__dot"></span>Dune Air &amp; Plus</p>
    <div class="contact-panel">
      <h1 class="contact-panel__name">Tom Harker</h1>
      <ul class="contact-list">
        <li class="contact-list__item">
          <svg class="contact-list__icon" viewBox="0 0 24 24" aria-hidden="true"><path d="M6.6 10.8a15.1 15.1 0 0 0 6.6 6.6l2.2-2.2a1 1 0 0 1 1-.25 11.4 11.4 0 0 0 3.6.57 1 1 0 0 1 1 1V20a1 1 0 0 1-1 1A17 17 0 0 1 3 4a1 1 0 0 1 1-1h3.5a1 1 0 0 1 1 1c0 1.25.2 2.45.57 3.57a1 1 0 0 1-.25 1z"/></svg>
          (623) 555-0142
        </li>
        <li class="contact-list__item">
          <svg class="contact-list__icon" viewBox="0 0 24 24" aria-hidden="true"><path d="M2 5h20v2l-10 6L2 7z"/><path d="M2 9.3l10 6 10-6V19H2z"/></svg>
          tom@trydunesair.com
        </li>
        <li class="contact-list__item">
          <svg class="contact-list__icon" viewBox="0 0 24 24" aria-hidden="true"><path d="M12 2a10 10 0 1 0 0 20 10 10 0 0 0 0-20zm6.9 6h-2.9a15.7 15.7 0 0 0-1.4-3.6A8 8 0 0 1 18.9 8zM12 4c.8 1.2 1.5 2.5 1.9 4h-3.8c.4-1.5 1.1-2.8 1.9-4zM4.3 14a8 8 0 0 1 0-4h3.4a16 16 0 0 0 0 4zm.8 2h2.9c.3 1.3.8 2.5 1.4 3.6A8 8 0 0 1 5.1 16zM8 8H5.1a8 8 0 0 1 4.3-3.6C8.8 5.5 8.3 6.7 8 8zm4 12c-.8-1.2-1.5-2.5-1.9-4h3.8c-.4 1.5-1.1 2.8-1.9 4zm2.3-6H9.7a14.6 14.6 0 0 1 0-4h4.6a14.6 14.6 0 0 1 0 4zm.3 5.6c.6-1.1 1.1-2.3 1.4-3.6h2.9a8 8 0 0 1-4.3 3.6zm1.7-5.6a16 16 0 0 0 0-4h3.4a8 8 0 0 1 0 4z"/></svg>
          www.trydunesair.com
        </li>
        <li class="contact-list__item">ROC 514273</li>
      </ul>
    </div>
  </section>
</main>
</body>
</html>
```